Velvor Display PowerPoint Design Project

We need PowerPoint slide templates for our Sales Media Kit at our re-branded company based in Canada called "Velvor Display Collective".

Looking for a look that clearly and powerfully portrays our unique and effective indoor advertising billboards in our network.

Our TinyPanes, WideSlats and GrandSheets are strategically placed in high traffic areas of restaurants, pubs, nightclubs, fitness clubs, colleges and universities, and sports arenas.

Key features of our media is a captive audience and 100% gender specific.

You can visit our old website for info on the above three media products (plorvex.ca)

Our Media Kits go out to small, medium business owners and advertising agenices.

Deliverables are:

1) Presentation cover slide with rich graphic content and space for content.
2) Presentation body slide with room for content 2 photos or logos. This slide should have the following:
a) No graphic in the text area
b) Space for page number at the bottom.
3) Photoshop (PSD) files for all graphic elements.
4) Font files for all fonts used.

Project Deadline Extended
Reason: Need more designs submitted.

We have uploaded our business card file.

Would like to incorporate the look, feel and colour of our business card to the power point template.

Target Market(s)

small business owners, marketing managers, media buyers and advertising agencies.

Industry/Entity Type

Advertising

Requirements
Must have
• We would like to see designs that:
- use the color scheme indicated by the attached logo design, perhaps expanding on it slightly.
- Look should be professional, smooth, and colourful.
-Must have a clean and modern feel that Ad Agencies would be impressed with.
-We have uploaded our business card file.

-Would like to incorporate the look, feel and colour of our business card to the power point template.

```html
<!DOCTYPE html>
<html lang="en">
<head>
<meta charset="utf-8">
<title>Content Slide</title>
<link href="https://fonts.googleapis.com/css2?family=Nunito:wght@800;900&family=Arimo:wght@400&display=swap" rel="stylesheet">
<style>
  :root {
    --navy: #0b1a33;
    --navy-deep: #060f22;
    --smoke: #3d6fb8;
    --smoke-light: #c9d6e8;
    --accent: #2e6cc2;
    --body-text: #595959;
    --footer-line: #b5b5b5;
    --white: #ffffff;
  }
  * { box-sizing: border-box; margin: 0; padding: 0; }
  html, body {
    width: 1200px;
    height: 900px;
    overflow: hidden;
    background: var(--white);
  }
  .slide {
    position: relative;
    width: 1200px;
    height: 900px;
    background: var(--white);
    border-left: 2px solid var(--navy);
    overflow: hidden;
  }
  .header {
    position: absolute;
    top: 0; left: 0;
    width: 100%;
    height: 104px;
    background: linear-gradient(180deg, var(--smoke-light) 0%, var(--navy) 14%, var(--navy-deep) 100%);
  }
  .header-smoke {
    position: absolute;
    inset: 0;
    background:
      radial-gradient(ellipse 260px 70px at 700px 30px, rgba(61,111,184,0.55), transparent 70%),
      radial-gradient(ellipse 200px 60px at 420px 10px, rgba(61,111,184,0.45), transparent 70%),
      radial-gradient(ellipse 180px 80px at 860px 70px, rgba(61,111,184,0.35), transparent 70%);
  }
  .slide-title {
    position: absolute;
    left: 40px;
    top: 34px;
    font-family: "Nunito", sans-serif;
    font-weight: 900;
    font-size: 44px;
    line-height: 1;
    color: var(--white);
    letter-spacing: 1px;
  }
  .brand {
    position: absolute;
    right: 40px;
    top: 32px;
    display: flex;
    align-items: center;
    gap: 10px;
    font-family: "Nunito", sans-serif;
    font-weight: 900;
    font-size: 34px;
    color: var(--white);
  }
  .brand-mark {
    width: 30px;
    height: 30px;
    background: var(--smoke);
  }
  .content {
    position: absolute;
    top: 137px;
    left: 66px;
    right: 40px;
    list-style: none;
    font-family: "Arimo", sans-serif;
    color: var(--body-text);
  }
  .point {
    position: relative;
    padding-left: 26px;
    font-size: 32px;
    line-height: 38px;
    margin-top: 16px;
  }
  .point:first-child { margin-top: 0; }
  .point::before {
    content: "•";
    position: absolute;
    left: 0;
    color: var(--accent);
  }
  .subpoints {
    list-style: none;
    margin-top: 20px;
    margin-left: 12px;
  }
  .subpoint {
    position: relative;
    padding-left: 44px;
    font-size: 27px;
    line-height: 34px;
    margin-top: 16px;
  }
  .subpoint:first-child { margin-top: 0; }
  .subpoint::before {
    content: "–";
    position: absolute;
    left: 0;
    color: var(--accent);
  }
  .footer-line {
    position: absolute;
    left: 0;
    right: 0;
    top: 844px;
    height: 6px;
    background: linear-gradient(180deg, var(--footer-line), #e8e8e8);
  }
  .footer-date, .page-number {
    position: absolute;
    top: 862px;
    font-family: "Arimo", sans-serif;
    font-size: 18px;
    color: var(--accent);
  }
  .footer-date { left: 50px; }
  .page-number { right: 46px; }
</style>
</head>
<body>
<main class="slide">
  <header class="header">
    <div class="header-smoke" role="img" aria-label="Soft blue smoke wisps over dark navy band"></div>
    <h1 class="slide-title">Content Slide Title</h1>
    <div class="brand"><span class="brand-mark"></span>Velvor</div>
  </header>

  <ul class="content">
    <li class="point">Lorem ipsum dolor sit amet, consectetur adipiscing elit. Vestibulum leo elit, vehicula eu tempus vel, posuere ac nisi.</li>
    <li class="point">Class aptent taciti sociosqu ad litora torquent per conubia nostra, per inceptos himenaeos.</li>
    <li class="point">Integer leo arcu, lacinia id lacinia sit amet, egestas sed lectus.
      <ul class="subpoints">
        <li class="subpoint">Donec ut purus et enim pretium commodo sed id magna. Class aptent taciti sociosqu ad litora torquent per conubia nostra, per inceptos himenaeos.</li>
        <li class="subpoint">Nullam felis ipsum, fermentum vitae sagittis id, semper sit amet felis. Quisque luctus sollicitudin libero, sit amet sodales enim scelerisque pulvinar.</li>
      </ul>
    </li>
    <li class="point">Class aptent taciti sociosqu ad litora torquent per conubia nostra, per inceptos himenaeos.</li>
    <li class="point">Duis fermentum neque et nisl tincidunt scelerisque.</li>
  </ul>

  <div class="footer-line"></div>
  <span class="footer-date">28-09-2012</span>
  <span class="page-number">2</span>
</main>
</body>
</html>
```